Plumbing Company business card design

Create a business card for our plumbing company. Following info needs to be present

Website-rivertoptapworks.net
Email- rivertoptapworks@mailnest.net
Phone-555-314-2098
Address-4876 NW Larkspur Blvd STE K
Cedar Hollow, Nebraska 50999

```html
<!DOCTYPE html>
<html lang="en">
<head>
<meta charset="utf-8">
<title>Rivertop Tapworks – Business Card</title>
<link href="https://fonts.googleapis.com/css2?family=Montserrat:wght@300;400;600;700&display=swap" rel="stylesheet">
<style>
  :root {
    --backdrop: #969696;
    --navy-light: #1b5a9a;
    --navy-dark: #123a63;
    --brand-red: #e8242b;
    --brand-blue: #1458a0;
    --white: #ffffff;
    --ink: #3a3a3a;
    --muted: #6f6f6f;
    --rule: #cfcfcf;
  }
  * { margin: 0; padding: 0; box-sizing: border-box; }
  html, body { width: 1200px; height: 1000px; overflow: hidden; }
  body {
    background: var(--backdrop);
    font-family: "Montserrat", sans-serif;
    position: relative;
  }
  .card {
    position: absolute;
    left: 293px;
    width: 615px;
    height: 350px;
    border-radius: 28px;
    overflow: hidden;
  }
  .card--front { top: 100px; background: var(--navy-dark); }
  .card--back { top: 511px; background: var(--white); }

  .front-pattern {
    position: absolute; inset: 0;
    background: linear-gradient(100deg, var(--navy-light) 0%, #174d85 45%, var(--navy-dark) 100%);
  }
  .front-brand {
    position: absolute; left: 0; right: 0; top: 115px;
    display: flex; flex-direction: column; align-items: center; gap: 20px;
  }
  .front-brand__mark {
    width: 70px; height: 70px; border-radius: 50%;
    background: var(--brand-red);
  }
  .front-brand__name {
    color: var(--white);
    font-weight: 700; font-size: 21px; letter-spacing: 1px;
  }

  .back-brand {
    position: absolute; left: 0; right: 0; top: 42px;
    display: flex; justify-content: center; align-items: center; gap: 9px;
  }
  .back-brand__mark {
    width: 48px; height: 48px; border-radius: 50%;
    background: var(--brand-blue);
  }
  .back-brand__name {
    color: var(--brand-red);
    font-weight: 700; font-size: 15px; letter-spacing: 0.5px;
  }

  .person {
    position: absolute; right: 354px; top: 180px; text-align: right;
  }
  .person__name {
    font-weight: 700; font-size: 16px; letter-spacing: 3px; color: var(--ink);
  }
  .person__role {
    font-weight: 300; font-size: 15px; letter-spacing: 2px; color: var(--ink); margin-top: 2px;
  }

  .contact {
    position: absolute; left: 301px; top: 167px;
    list-style: none;
  }
  .contact__item {
    display: flex; align-items: center; gap: 10px;
    font-size: 15px; color: var(--muted); height: 23px;
  }
  .contact__icon { width: 16px; height: 14px; flex: none; }

  .address-rule {
    position: absolute; left: 44px; right: 42px; top: 297px;
    border-top: 1px solid var(--rule);
  }
  .address {
    position: absolute; left: 0; right: 0; top: 311px;
    text-align: center; font-size: 15px; color: var(--muted);
  }
</style>
</head>
<body>
  <section class="card card--front">
    <div class="front-pattern" role="img" aria-label="Repeating faint brand mark pattern in blue tones"></div>
    <div class="front-brand">
      <div class="front-brand__mark"></div>
      <div class="front-brand__name">RIVERTOP TAPWORKS</div>
    </div>
  </section>

  <section class="card card--back">
    <div class="back-brand">
      <div class="back-brand__mark"></div>
      <div class="back-brand__name">RIVERTOP TAPWORKS</div>
    </div>

    <div class="person">
      <div class="person__name">NAME SURNAME</div>
      <div class="person__role">Position</div>
    </div>

    <ul class="contact">
      <li class="contact__item">
        <svg class="contact__icon" viewBox="0 0 16 16"><rect x="4" y="0.5" width="8" height="15" rx="1.5" fill="none" stroke="#e8242b" stroke-width="1.6"/><circle cx="8" cy="12.8" r="1" fill="#e8242b"/></svg>
        555-314-2098
      </li>
      <li class="contact__item">
        <svg class="contact__icon" viewBox="0 0 16 12"><rect x="0" y="1" width="16" height="10" fill="#e8242b"/><path d="M0 1 L8 7 L16 1" fill="none" stroke="#fff" stroke-width="1.2"/></svg>
        rivertoptapworks@mailnest.net
      </li>
      <li class="contact__item">
        <svg class="contact__icon" viewBox="0 0 16 16"><circle cx="8" cy="8" r="6.5" fill="none" stroke="#e8242b" stroke-width="1.4"/><ellipse cx="8" cy="8" rx="3" ry="6.5" fill="none" stroke="#e8242b" stroke-width="1.2"/><path d="M1.5 8 H14.5 M2.5 4.8 H13.5 M2.5 11.2 H13.5" stroke="#e8242b" stroke-width="1.1"/></svg>
        rivertoptapworks.net
      </li>
    </ul>

    <div class="address-rule"></div>
    <p class="address">4876 NW Larkspur Blvd STE K Cedar Hollow, Nebraska 50999</p>
  </section>
</body>
</html>
```